Brochure for Varesh Law firm

We would like to have a brochure that describes the Firm ( about the firm) , the vision, the team , the practice areas. And the contact.
Varesh law firm has ranked as top Libyan law firms by Juris Ledger.
It will give a good picture if you look at www.varesh-example.ly

We can also provide more information if requested to share with designer.

```html
<!DOCTYPE html>
<html lang="en">
<head>
<meta charset="utf-8">
<title>Varesh Law firm – Brochure</title>
<link href="https://fonts.googleapis.com/css2?family=Poppins:wght@300;400;500;600;700;800&family=Montserrat:wght@400;500&display=swap" rel="stylesheet">
<style>
:root{
  --blue:#0c3fc0;
  --blue-dark:#08309a;
  --ink:#111111;
  --black:#0d0d0d;
  --paper:#f3f3f4;
  --text:#2a2a2a;
  --canvas:#e6e6e7;
  --white:#ffffff;
}
*{box-sizing:border-box;margin:0;padding:0}
html,body{width:1200px;height:2347px;overflow:hidden;background:var(--canvas)}
body{position:relative;font-family:'Montserrat',sans-serif;color:var(--text)}
.spread{position:absolute;left:30px;width:1140px;height:805px;display:flex;box-shadow:0 12px 28px rgba(0,0,0,.18)}
.spread--outside{top:338px}
.spread--inside{top:1203px}
.panel{position:relative;width:380px;height:805px;overflow:hidden}
.panel--light{background:var(--paper)}
.panel--dark{background:var(--black);color:var(--white)}
.panel--blue{background:var(--blue);color:var(--white)}
.heading{font-family:'Poppins',sans-serif;font-weight:700;font-size:23px;color:var(--ink);letter-spacing:.2px;line-height:1}
.heading em{font-style:normal;color:var(--blue)}
.body{font-size:10.4px;line-height:1.27;text-align:justify}

/* vision */
.vision{padding:44px 34px 0 34px}
.vision .body{margin-top:8px}
.vision .body + .body{margin-top:12px}
.pillars-intro{margin-top:30px;font-family:'Poppins',sans-serif;font-weight:300;font-size:15px;color:var(--ink);line-height:1.1}
.pillars-intro strong{display:block;color:var(--blue);font-weight:700}
.pillars{list-style:none;margin-top:14px}
.pillars li{display:flex;gap:7px;font-size:10.4px;line-height:1.27;text-align:justify;margin-bottom:9px}
.pillars svg{flex:0 0 14px;margin-top:1px}

/* contact */
.brand{font-family:'Poppins',sans-serif;font-weight:500;letter-spacing:1px;line-height:1}
.contact .brand{position:absolute;top:125px;left:0;right:0;text-align:center;font-size:38px;color:var(--white)}
.office{position:absolute;left:60px;width:260px;border:1px solid #555;border-radius:6px;background:#111;text-align:center}
.office--tripoli{top:220px}
.office--benghazi{top:468px}
.office-title{background:#d9d9d9;color:#222;font-family:'Poppins',sans-serif;font-weight:600;font-size:24px;padding:4px 0;border-radius:5px 5px 0 0}
.office-body{padding:14px 14px 16px}
.office-addr{font-size:14px;line-height:1.2;color:#eee;margin-top:6px}
.office-phone{font-family:'Poppins',sans-serif;font-weight:700;font-size:27px;margin-top:8px;color:var(--white);border-top:1px dotted #444;padding-top:6px}
.web{position:absolute;left:0;right:0;text-align:center;font-family:'Poppins',sans-serif;font-size:16px;letter-spacing:4px}
.web b{color:var(--blue);font-weight:600}
.contact .web{bottom:30px;color:var(--white)}
.globe{position:absolute;bottom:58px;left:180px}

/* cover */
.cover .brand{position:absolute;top:45px;left:0;right:0;text-align:center;font-size:44px;color:var(--ink)}
.cover-title{position:absolute;top:127px;left:0;right:0;text-align:center;font-family:'Poppins',sans-serif;line-height:.95}
.cover-title .light{display:block;font-weight:300;font-size:37px;color:var(--ink)}
.cover-title .strong{display:block;font-weight:800;font-size:52px;color:var(--ink)}
.cover-title .accent{display:block;font-weight:800;font-size:56px;color:var(--blue)}
.cover-rule{position:absolute;top:284px;left:160px;width:60px;height:6px;background:var(--ink);border-radius:3px}
.tagline{position:absolute;top:305px;left:50px;right:50px;text-align:center;font-family:'Poppins',sans-serif;font-size:16px;color:var(--ink);line-height:1.25}
.cover-photo{position:absolute;top:355px;left:0;width:380px;height:406px}
.cover-bar{position:absolute;bottom:0;left:0;width:380px;height:44px;background:var(--black)}
.cover .web{bottom:12px;color:var(--white)}

/* services */
.services{padding:44px 36px 0}
.services .heading{color:var(--white)}
.services .lead{font-size:11px;line-height:1.2;margin-top:6px;color:#e6ebff}
.service-row{display:flex;justify-content:space-around;padding:20px 0 18px;border-bottom:1px dotted rgba(255,255,255,.45)}
.service-row:last-of-type{border-bottom:none;justify-content:center;gap:40px}
.service{width:100px;text-align:center;font-family:'Poppins',sans-serif;font-weight:600;font-size:12.5px;line-height:1.15}
.service svg{display:block;margin:0 auto 8px}
.gavel-photo{position:absolute;left:0;bottom:0;width:380px;height:250px}

/* firm */
.firm{padding:44px 34px 0}
.sub{margin-top:20px;font-family:'Poppins',sans-serif;font-weight:600;font-size:15px;color:var(--blue);border-left:2px solid var(--blue);padding-left:5px;line-height:1}
.firm .body{margin-top:9px;font-size:10.2px}
.firm .body + .body{margin-top:14px}
.badges{position:absolute;left:34px;right:34px;bottom:44px;display:grid;grid-template-columns:repeat(4,1fr);gap:16px 14px}
.badge{height:14px;border-radius:3px;background:#cfcfd2}

/* testimonials */
.testimonials{padding:44px 34px 0}
.quote{position:relative;margin-top:34px;border:1.5px dashed #9aa0ad;border-radius:6px;padding:24px 16px 10px}
.quote-mark{position:absolute;top:-16px;left:12px;background:var(--paper);padding:0 4px;line-height:0}
.quote .body{font-size:10.4px}
.quote-source{text-align:right;font-family:'Poppins',sans-serif;font-weight:700;font-size:15px;color:var(--blue);margin-top:6px}
.team{margin-top:26px}
.members{display:flex;justify-content:space-between;margin-top:10px}
.member{width:100px;text-align:center}
.portrait{width:72px;height:72px;border-radius:50%;margin:0 auto;background:linear-gradient(160deg,#d6d6d6,#6f6f6f);border:3px solid var(--blue)}
.member-name{font-family:'Poppins',sans-serif;font-weight:600;font-size:12.5px;line-height:1.1;margin-top:8px;color:var(--ink)}
.member-role{font-size:9px;color:#444;margin-top:4px}
</style>
</head>
<body>

<section class="spread spread--outside">
  <article class="panel panel--light vision">
    <h2 class="heading">THE <em>VISION</em></h2>
    <p class="body">Libya has gone through many profound changes since we first opened our doors in 2005. Throughout this time of far-reaching transformation, we have always been driven by an entrepreneurial and socially conscious spirit, embracing change in order to help shape the future. This is why we chose to keep investing in the Libyan market when others would not. Now the same values will drive where we go next. We will remain independent and in control of our destiny so that we can continue to provide first-class legal services to our clients from around the world, to sit alongside them as a trusted advisor and to passionately guard their interests by helping to settle their disputes, protect their assets and grow their businesses.</p>
    <p class="body">But in addition to this, we believe that lawyers are key agents of social change who have a responsibility to promote innovation, sustainability and economic and social development. Therefore, in order to become the law firm that can best help our clients – and our own people – prepare for and shape the future of Libya, we believe that we must break free from the traditional models that currently dominate the Libyan legal market.</p>
    <p class="pillars-intro">TO ACHIEVE THIS WE HAVE ADOPTED <strong>A 2021–2025 VISION THAT INCLUDES<br>FOUR MAIN PILLARS</strong></p>
    <ul class="pillars">
      <li><svg width="14" height="14" viewBox="0 0 14 14"><circle cx="7" cy="7" r="6" fill="none" stroke="#0c3fc0" stroke-width="1.2"/><path d="M4 7.2l2 2 4-4" fill="none" stroke="#0c3fc0" stroke-width="1.3"/></svg><span>We aim to become Libya's first truly national full-service law firm, building on our existing presence in London, Tripoli and Benghazi to cover all major business centres and practice areas.</span></li>
      <li><svg width="14" height="14" viewBox="0 0 14 14"><circle cx="7" cy="7" r="6" fill="none" stroke="#0c3fc0" stroke-width="1.2"/><path d="M4 7.2l2 2 4-4" fill="none" stroke="#0c3fc0" stroke-width="1.3"/></svg><span>We aim to become Libya's first truly digitalized law firm, creating a technology platform to automate routine tasks and processes so that our professionals can focus more on value-added client services and their own professional development.</span></li>
      <li><svg width="14" height="14" viewBox="0 0 14 14"><circle cx="7" cy="7" r="6" fill="none" stroke="#0c3fc0" stroke-width="1.2"/><path d="M4 7.2l2 2 4-4" fill="none" stroke="#0c3fc0" stroke-width="1.3"/></svg><span>We aim to become Libya's first true legal partnership, ensuring that all of our professionals will have an equity stake in our business because we believe that this will help us attract the best young legal talent, promote an equitable workplace and sustain our growth far into the future.</span></li>
      <li><svg width="14" height="14" viewBox="0 0 14 14"><circle cx="7" cy="7" r="6" fill="none" stroke="#0c3fc0" stroke-width="1.2"/><path d="M4 7.2l2 2 4-4" fill="none" stroke="#0c3fc0" stroke-width="1.3"/></svg><span>We aim to become Libya's most socially responsible law firm. We have always been committed to having a positive impact on both our local communities and the wider world and we recently became the first Libyan firm to require its professionals to spend at least% of their time on social impact and pro bono activities.</span></li>
    </ul>
  </article>

  <article class="panel panel--dark contact">
    <div class="brand">Varesh</div>
    <div class="office office--tripoli">
      <div class="office-title">Tripoli Office</div>
      <div class="office-body">
        <svg width="22" height="24" viewBox="0 0 22 24"><path d="M11 2a7 7 0 0 0-7 7c0 5 7 13 7 13s7-8 7-13a7 7 0 0 0-7-7z" fill="none" stroke="#1c55e6" stroke-width="2"/><circle cx="11" cy="9" r="2.5" fill="#1c55e6"/></svg>
        <p class="office-addr">12, Harbour Plaza PO. Box 40100<br>Tripoli, Libya</p>
        <svg width="20" height="20" viewBox="0 0 20 20" style="margin-top:8px"><path d="M5 2l3 4-2 2c1 2 3 4 5 5l2-2 4 3-2 3C9 17 3 11 2 5z" fill="#1c55e6"/></svg>
        <p class="office-phone">+218 21 5550140</p>
      </div>
    </div>
    <div class="office office--benghazi">
      <div class="office-title">Benghazi Office</div>
      <div class="office-body">
        <svg width="22" height="24" viewBox="0 0 22 24"><path d="M11 2a7 7 0 0 0-7 7c0 5 7 13 7 13s7-8 7-13a7 7 0 0 0-7-7z" fill="none" stroke="#1c55e6" stroke-width="2"/><circle cx="11" cy="9" r="2.5" fill="#1c55e6"/></svg>
        <p class="office-addr">Shari' Al Noor, Block 7,<br>Eastern District. Benghazi,<br>Libya.</p>
        <svg width="20" height="20" viewBox="0 0 20 20" style="margin-top:6px"><path d="M5 2l3 4-2 2c1 2 3 4 5 5l2-2 4 3-2 3C9 17 3 11 2 5z" fill="#1c55e6"/></svg>
        <p class="office-phone">+218 92 555 0187</p>
      </div>
    </div>
    <svg class="globe" width="20" height="20" viewBox="0 0 20 20"><circle cx="10" cy="10" r="8.5" fill="none" stroke="#1c55e6" stroke-width="1.8"/><path d="M1.5 10h17M10 1.5c-4 4.5-4 12.5 0 17M10 1.5c4 4.5 4 12.5 0 17" fill="none" stroke="#1c55e6" stroke-width="1.5"/></svg>
    <div class="web">www.<b>varesh-example</b>.ly</div>
  </article>

  <article class="panel panel--light cover">
    <div class="brand">Varesh</div>
    <h1 class="cover-title"><span class="light">SETTING THE</span><span class="strong">STANDARD</span><span class="accent">FOR LIBYA</span></h1>
    <div class="cover-rule"></div>
    <p class="tagline">Excellence is the hallmark of our legal solutions</p>
    <svg class="cover-photo" viewBox="0 0 380 406" role="img" aria-label="Photo of a smiling lawyer in a navy suit holding a tablet">
      <defs><linearGradient id="coverTone" x1="0" y1="0" x2="1" y2="1"><stop offset="0" stop-color="#c9c3bd"/><stop offset="1" stop-color="#1b2744"/></linearGradient></defs>
      <polygon points="0,35 380,0 380,406 0,406" fill="var(--blue)"/>
      <path d="M120,406 L140,110 Q200,10 290,60 L330,406 Z" fill="url(#coverTone)"/>
    </svg>
    <div class="cover-bar"></div>
    <div class="web">www.<b>varesh-example</b>.ly</div>
  </article>
</section>

<section class="spread spread--inside">
  <article class="panel panel--blue services">
    <h2 class="heading">OUR SERVICES</h2>
    <p class="lead">Varesh Law provides professional legal consultants and services to our individual and corporate clients.</p>
    <div class="service-row">
      <div class="service"><svg width="54" height="54" viewBox="0 0 54 54"><circle cx="27" cy="27" r="25" fill="#fff" stroke="#08309a" stroke-width="2"/><rect x="15" y="16" width="24" height="15" rx="3" fill="none" stroke="#0c3fc0" stroke-width="2"/><path d="M20 31l-3 6 8-6" fill="none" stroke="#0c3fc0" stroke-width="2"/></svg>Consultation</div>
      <div class="service"><svg width="54" height="54" viewBox="0 0 54 54"><circle cx="27" cy="27" r="25" fill="#fff" stroke="#08309a" stroke-width="2"/><path d="M15 24l12-8 12 8M18 24v12M24 24v12M30 24v12M36 24v12M15 38h24" fill="none" stroke="#0c3fc0" stroke-width="2"/></svg>Litigation</div>
      <div class="service"><svg width="54" height="54" viewBox="0 0 54 54"><circle cx="27" cy="27" r="25" fill="#fff" stroke="#08309a" stroke-width="2"/><path d="M17 36l12-12M24 19l9 9M28 15l9 9M15 39h14" fill="none" stroke="#0c3fc0" stroke-width="2.4"/></svg>Arbitration</div>
    </div>
    <div class="service-row">
      <div class="service"><svg width="54" height="54" viewBox="0 0 54 54"><circle cx="27" cy="27" r="25" fill="#fff" stroke="#08309a" stroke-width="2"/><circle cx="27" cy="24" r="8" fill="none" stroke="#0c3fc0" stroke-width="2"/><path d="M15 38h24" stroke="#0c3fc0" stroke-width="2"/></svg>Commercial Registration</div>
      <div class="service"><svg width="54" height="54" viewBox="0 0 54 54"><circle cx="27" cy="27" r="25" fill="#fff" stroke="#08309a" stroke-width="2"/><path d="M18 38V30M24 38V26M30 38V22M36 38V17M16 30l20-13" fill="none" stroke="#0c3fc0" stroke-width="2.4"/></svg>Investment Licence</div>
      <div class="service"><svg width="54" height="54" viewBox="0 0 54 54"><circle cx="27" cy="27" r="25" fill="#fff" stroke="#08309a" stroke-width="2"/><path d="M27 14v24M16 19h22M16 19l-4 10h8zM38 19l-4 10h8zM21 38h12" fill="none" stroke="#0c3fc0" stroke-width="2"/></svg>Legal Risk Assessment</div>
    </div>
    <div class="service-row">
      <div class="service"><svg width="54" height="54" viewBox="0 0 54 54"><circle cx="27" cy="27" r="25" fill="#fff" stroke="#08309a" stroke-width="2"/><path d="M13 26l7-5 7 4 7-4 7 5-9 9-5-3-5 3z" fill="none" stroke="#0c3fc0" stroke-width="2"/></svg>Due-Diligence</div>
      <div class="service"><svg width="54" height="54" viewBox="0 0 54 54"><circle cx="27" cy="27" r="25" fill="#fff" stroke="#08309a" stroke-width="2"/><path d="M15 27l12-11 12 11M18 25v13h18V25" fill="none" stroke="#0c3fc0" stroke-width="2"/><circle cx="27" cy="31" r="3" fill="#0c3fc0"/></svg>Intellectual Property</div>
    </div>
    <svg class="gavel-photo" viewBox="0 0 380 250" role="img" aria-label="Photo of a wooden judge's gavel on its block">
      <defs><linearGradient id="gavelTone" x1="0" y1="0" x2="0" y2="1"><stop offset="0" stop-color="#d9d9db"/><stop offset="1" stop-color="#8e8e92"/></linearGradient></defs>
      <polygon points="0,40 380,0 380,250 0,250" fill="url(#gavelTone)"/>
      <ellipse cx="150" cy="215" rx="90" ry="26" fill="#2a1d17"/>
    </svg>
  </article>

  <article class="panel panel--light firm">
    <h2 class="heading"><em>THE FIRM</em></h2>
    <h3 class="sub">Since 2005</h3>
    <p class="body">Varesh Law is a law firm established in Tripoli, Libya, in 2005. The Firm brings together some of the most experienced legal practitioners and scholars in Libya. In addition to our head offices in Tripoli, our first regional office was launched in Benghazi.</p>
    <h3 class="sub">Expertise</h3>
    <p class="body">Our lawyers and consultants have over 200 years of combined legal experience. Our client base includes Apex 500 companies, Tech Corridor heavyweights, State Legal departments of leading nations, and other corporate clients from around the world.</p>
    <h3 class="sub">Juris Ledger</h3>
    <p class="body">Varesh Law is currently featured s Libya's Leading Tier 1 law firm in the Juris Ledger EMEA 2020 rankings. We have been appointed by the Northbridge State Legal Office as Legal Experts on various high-profile Libyan cases. We are also members of the advisory board to the Libyan Forum for International Commercial Arbitration.</p>
    <h3 class="sub">Activities</h3>
    <p class="body">The Team is active in academic and humanitarian fields, whether contributing to reputable publications such as the Meridian International Tax Guide and Lexora MENA Business Law Review or supporting regional efforts to tackle human trafficking and illegal migration in Libya, among various other noteworthy initiatives.</p>
    <p class="body">The Team has previously worked with the Halden Centre for International Justice and Ashby Crane on the Halden Centre Environment Program. This was a Comprehensive Research program on the Right to a Healthy Environment with the Independent Rapporteur on Human Rights and the Environment.</p>
    <div class="badges">
      <span class="badge"></span><span class="badge"></span><span class="badge"></span><span class="badge"></span>
      <span class="badge"></span><span class="badge"></span><span class="badge"></span><span class="badge"></span>
    </div>
  </article>

  <article class="panel panel--light testimonials">
    <h2 class="heading">CLIENT'S <em>TESTIMONIALS</em></h2>
    <div class="quote">
      <span class="quote-mark"><svg width="34" height="28" viewBox="0 0 34 28"><path d="M2 28V14C2 6 6 2 14 0v6c-4 1-5 4-5 8h5v14zM19 28V14c0-8 4-12 12-14v6c-4 1-5 4-5 8h5v14z" fill="#0c3fc0"/></svg></span>
      <p class="body">Varesh Law operates in a genuine niche as a law firm providing international law firm levels of support and responsiveness in connection with the Libyan jurisdiction.</p>
      <p class="quote-source">JURIS LEDGER</p>
    </div>
    <div class="quote">
      <span class="quote-mark"><svg width="34" height="28" viewBox="0 0 34 28"><path d="M2 28V14C2 6 6 2 14 0v6c-4 1-5 4-5 8h5v14zM19 28V14c0-8 4-12 12-14v6c-4 1-5 4-5 8h5v14z" fill="#0c3fc0"/></svg></span>
      <p class="body">Karim Saadawi has unrivalled expertise in the Libyan legal market. He also has excellent local knowledge which informs his legal advice. We consider Varesh to be the premier law firm in this market.</p>
      <p class="quote-source">JURIS LEDGER</p>
    </div>
    <div class="quote">
      <span class="quote-mark"><svg width="34" height="28" viewBox="0 0 34 28"><path d="M2 28V14C2 6 6 2 14 0v6c-4 1-5 4-5 8h5v14zM19 28V14c0-8 4-12 12-14v6c-4 1-5 4-5 8h5v14z" fill="#0c3fc0"/></svg></span>
      <p class="body">In-depth knowledge of Libyan laws and regulations… practical know-how of how the Libyan public sector actually functions In Libya, the procedural, registration and documentary requirements associated with a transaction are often opaque and it is essential to seek guidance from an adviser who can offer more than a purely written analysis of the laws themselves.</p>
      <p class="quote-source">JURIS LEDGER</p>
    </div>
    <div class="team">
      <h2 class="heading"><em>OUR TEAM</em></h2>
      <div class="members">
        <div class="member"><div class="portrait" role="img" aria-label="Portrait of the founding partner"></div><p class="member-name">Karim<br>Saadawi</p><p class="member-role">Founding Partner</p></div>
        <div class="member"><div class="portrait" role="img" aria-label="Portrait of the managing partner"></div><p class="member-name">Tarek<br>Mansouri</p><p class="member-role">Managing Partner</p></div>
        <div class="member"><div class="portrait" role="img" aria-label="Portrait of a partner"></div><p class="member-name">Nabil<br>Ferjani</p><p class="member-role">Partner</p></div>
      </div>
    </div>
  </article>
</section>

</body>
</html>
```